Business card design for crowd sourced review site.

I need a business card magnet design for an online, crowd-sourced, restaurant review site strictly for Kosher restaurants.
It is similar to RoamLedger but catering to a very particular crowd.
The markets it will be distributed in are flooded with business card fridge magnets so this needs to be eye-catching and unique. The Business name is PlateMarks
The website isnt finished but you can see the basic setup here
http://restaurant.vintrello.com/

The second image i included is another logo design I liked and was thinking about using and decided I will probably also make a SECOND custom cut business card in the shape of that icon. Bonus if you can throw that in also.

Target Market(s)

Jewish consumers aged 20-35

Industry/Entity Type

Business

Contact Information for Business Card

see description.
Design should not be too crowded and should in eye-catching. Will mainly be used as fridge magnets.

Requirements
Must have
• Website address. logo.
Nice to have
• tagline. (The Definitive guide to kosher dining for the Kosher consumer)
• Im not a professional but I personally think the color blue goes along with this concept. ill leave it to you to decide.
Should not have
• any religious symbols.

```html
<!DOCTYPE html>
<html lang="en">
<head>
<meta charset="utf-8">
<title>PlateMarks business card</title>
<link href="https://fonts.googleapis.com/css2?family=Open+Sans:wght@400;600&display=swap" rel="stylesheet">
<style>
  :root {
    --page-bg: #e9e6e1;
    --card-black: #1b1b1b;
    --card-black-light: #2c2c2c;
    --strip-grey: #c9c9c9;
    --card-white: #f1f1f1;
    --accent-red: #e0503c;
    --text-dark: #4a4a4a;
    --text-white: #ffffff;
    --logo-faint: #d9d9d9;
  }
  * { box-sizing: border-box; margin: 0; padding: 0; }
  html, body { width: 1200px; height: 1023px; overflow: hidden; }
  body {
    background: var(--page-bg);
    font-family: "Open Sans", Arial, sans-serif;
    position: relative;
  }
  .card {
    position: absolute;
    top: 356px;
    width: 540px;
    height: 310px;
    border-radius: 18px;
    overflow: hidden;
    box-shadow: 0 10px 24px rgba(0,0,0,0.22);
  }
  /* Front */
  .card-front {
    left: 40px;
    background: radial-gradient(ellipse at 55% 40%, var(--card-black-light), var(--card-black) 70%);
  }
  .front-brand {
    position: absolute;
    left: 0; right: 0; top: 92px;
    display: flex; align-items: center; justify-content: center; gap: 16px;
  }
  .brand-dot {
    width: 34px; height: 34px; border-radius: 50%;
    background: var(--accent-red);
  }
  .front-brand .brand-name {
    font-size: 62px; font-weight: 600; color: var(--text-white); letter-spacing: 1px;
  }
  .tagline-strip {
    position: absolute; left: 0; right: 0; bottom: 0; height: 48px;
    background: var(--strip-grey);
    display: flex; align-items: center; justify-content: center;
  }
  .tagline {
    font-size: 16px; color: var(--accent-red); letter-spacing: 0.5px;
  }
  /* Back */
  .card-back {
    left: 620px;
    background: var(--card-white);
  }
  .name-pill {
    position: absolute; left: 0; top: 22px;
    width: 300px; height: 74px;
    background: var(--accent-red);
    border-radius: 0 37px 37px 0;
    padding: 12px 0 0 150px;
    color: var(--text-white);
  }
  .name-pill .person-name { font-size: 20px; line-height: 1.1; }
  .name-pill .person-title { font-size: 12px; color: #3a1a14; }
  .contact-list {
    position: absolute; left: 34px; top: 118px;
    list-style: none;
  }
  .contact-list li {
    display: flex; align-items: center; gap: 10px;
    font-size: 14px; color: var(--text-dark); line-height: 24px;
  }
  .contact-list svg { width: 12px; height: 12px; flex: none; }
  .back-brand {
    position: absolute; right: 40px; bottom: 36px;
    display: flex; align-items: center; gap: 10px;
  }
  .back-brand .brand-dot { width: 20px; height: 20px; }
  .back-brand .brand-name {
    font-size: 34px; font-weight: 600; color: var(--logo-faint);
  }
</style>
</head>
<body>
  <section class="card card-front">
    <div class="front-brand">
      <span class="brand-dot"></span>
      <span class="brand-name">PlateMarks</span>
    </div>
    <div class="tagline-strip">
      <p class="tagline">The Definitive guide to kosher dining for the Kosher consumer</p>
    </div>
  </section>

  <section class="card card-back">
    <div class="name-pill">
      <p class="person-name">Your Name</p>
      <p class="person-title">Title</p>
    </div>
    <ul class="contact-list">
      <li>
        <svg viewBox="0 0 12 12"><path d="M6 0a4 4 0 0 1 4 4c0 3-4 8-4 8S2 7 2 4a4 4 0 0 1 4-4z" fill="var(--accent-red)"/><circle cx="6" cy="4" r="1.5" fill="#fff"/></svg>
        Your address
      </li>
      <li>
        <svg viewBox="0 0 12 12"><circle cx="6" cy="6" r="5" fill="none" stroke="var(--accent-red)" stroke-width="1.2"/><path d="M4 3.5l1 1-0.6 1 1.6 1.6 1-0.6 1 1-1 1C5.5 8.5 3.5 6.5 3 5z" fill="var(--accent-red)"/></svg>
        (123)123-456
      </li>
      <li>
        <svg viewBox="0 0 12 12"><rect x="1" y="2.5" width="10" height="7" fill="none" stroke="var(--accent-red)" stroke-width="1.2"/><path d="M1 2.5l5 4 5-4" fill="none" stroke="var(--accent-red)" stroke-width="1.2"/></svg>
        info@restaurant.vintrello.com
      </li>
      <li>
        <svg viewBox="0 0 12 12"><circle cx="6" cy="6" r="5" fill="none" stroke="var(--accent-red)" stroke-width="1.2"/><path d="M1 6h10M6 1c-2.5 3-2.5 7 0 10M6 1c2.5 3 2.5 7 0 10" fill="none" stroke="var(--accent-red)" stroke-width="1"/></svg>
        www.restaurant.vintrello.com
      </li>
    </ul>
    <div class="back-brand">
      <span class="brand-dot"></span>
      <span class="brand-name">PlateMarks</span>
    </div>
  </section>
</body>
</html>
```